Bref créative
VPrestige
Vantorel Prestige
Professional
Marc Lindqvora
President
47219 Brookfern Hollow Lane
Larkmont, Ohio 30982
mlind@vantorelprestige.example
www.vantorelprestige.example
Need business card and stationary design. Have uploaded new logo.

```html
<!DOCTYPE html>
<html lang="en">
<head>
<meta charset="utf-8">
<title>Vantorel Prestige — Stationery</title>
<link href="https://fonts.googleapis.com/css2?family=Roboto+Condensed:wght@400;700&display=swap" rel="stylesheet">
<style>
  :root {
    --backdrop: #2b2927;
    --paper: #ffffff;
    --navy: #1b1f6e;
    --gold: #c9a04a;
    --gold-light: #ecd290;
    --ink: #4a4a58;
  }
  * { box-sizing: border-box; margin: 0; padding: 0; }
  html, body { width: 1200px; height: 961px; overflow: hidden; }
  body {
    position: relative;
    background: var(--backdrop);
    font-family: "Roboto Condensed", Arial, sans-serif;
    color: var(--ink);
  }
  .sheet {
    position: absolute;
    background: var(--paper);
    overflow: hidden;
    box-shadow: 0 6px 18px rgba(0,0,0,.35);
  }
  .gold-bar {
    position: absolute; left: 0; top: 0; width: 100%;
    background: linear-gradient(90deg, var(--gold), var(--gold-light) 50%, var(--gold));
  }
  .swoosh { position: absolute; left: 0; bottom: 0; width: 100%; display: block; }
  .brand { position: absolute; display: flex; align-items: center; gap: 6px; }
  .brand-dot { border-radius: 50%; background: var(--gold); flex: none; }
  .brand-name { color: var(--navy); font-weight: 700; white-space: nowrap; letter-spacing: -.2px; }
  .contact { position: absolute; font-style: normal; line-height: 1.35; color: var(--ink); white-space: nowrap; }
  .web { position: absolute; color: var(--gold); white-space: nowrap; }

  /* letterhead */
  .letterhead { left: 47px; top: 52px; width: 680px; height: 875px; }
  .letterhead .gold-bar { height: 9px; }
  .letterhead .brand { left: 62px; top: 36px; }
  .letterhead .brand-dot { width: 20px; height: 20px; }
  .letterhead .brand-name { font-size: 20px; }
  .letterhead .contact { left: 88px; top: 66px; font-size: 9px; }
  .letterhead .swoosh { height: 90px; }
  .letterhead .web { left: 420px; bottom: 20px; font-size: 9px; }

  /* envelope */
  .envelope { left: 397px; top: 122px; width: 753px; height: 333px; }
  .envelope .gold-bar { height: 8px; }
  .envelope .brand { left: 42px; top: 58px; }
  .envelope .brand-dot { width: 22px; height: 22px; }
  .envelope .brand-name { font-size: 22px; }
  .envelope .contact { left: 72px; top: 92px; font-size: 9px; }
  .envelope .swoosh { height: 88px; }
  .envelope .web { right: 30px; bottom: 30px; font-size: 9px; }

  /* business cards */
  .card { top: 486px; width: 278px; height: 163px; }
  .card .gold-bar { height: 6px; }
  .card .swoosh { height: 58px; }
  .card-front { left: 566px; }
  .card-front .brand { left: 14px; top: 24px; }
  .card-front .brand-dot { width: 14px; height: 14px; }
  .card-front .brand-name { font-size: 14px; }
  .card-front .contact { left: 32px; top: 46px; font-size: 7px; }
  .card-front .holder {
    position: absolute; left: 112px; bottom: 12px;
    font-size: 10px; color: #fff; font-weight: 700; white-space: nowrap;
  }
  .card-front .holder .title { color: var(--gold); font-weight: 400; }
  .card-back { left: 870px; }
  .card-back .web { right: 22px; bottom: 20px; font-size: 9px; }
</style>
</head>
<body>

  <section class="sheet letterhead" aria-label="Letterhead">
    <div class="gold-bar"></div>
    <div class="brand"><span class="brand-dot"></span><span class="brand-name">VantorelPrestige</span></div>
    <address class="contact">
      47219 Brookfern Hollow Lane<br>
      Larkmont, Ohio 30982<br>
      P: 555-201-0142<br>
      E: mlind@vantorelprestige.example
    </address>
    <svg class="swoosh" viewBox="0 0 680 90" preserveAspectRatio="none" aria-hidden="true">
      <defs>
        <linearGradient id="lh-band" x1="0" y1="0" x2="1" y2="0">
          <stop offset="0" stop-color="#3a56c9"/>
          <stop offset=".5" stop-color="#1f2a8a"/>
          <stop offset="1" stop-color="#10134a"/>
        </linearGradient>
      </defs>
      <path d="M0 62 C240 48 480 26 680 0 L680 90 L0 90 Z" fill="url(#lh-band)"/>
      <path d="M0 62 C240 48 480 26 680 0" fill="none" stroke="#c9a04a" stroke-width="1.2" opacity=".6"/>
    </svg>
    <span class="web">www.vantorelprestige.example</span>
  </section>

  <section class="sheet envelope" aria-label="Envelope">
    <div class="gold-bar"></div>
    <div class="brand"><span class="brand-dot"></span><span class="brand-name">VantorelPrestige</span></div>
    <address class="contact">
      47219 Brookfern Hollow Lane<br>
      Larkmont, Ohio 30982
    </address>
    <svg class="swoosh" viewBox="0 0 753 88" preserveAspectRatio="none" aria-hidden="true">
      <defs>
        <linearGradient id="env-band" x1="0" y1="0" x2="1" y2="0">
          <stop offset="0" stop-color="#3a56c9"/>
          <stop offset=".5" stop-color="#1f2a8a"/>
          <stop offset="1" stop-color="#10134a"/>
        </linearGradient>
      </defs>
      <path d="M0 70 C280 62 540 34 753 0 L753 88 L0 88 Z" fill="url(#env-band)"/>
      <path d="M0 70 C280 62 540 34 753 0" fill="none" stroke="#c9a04a" stroke-width="1.2" opacity=".6"/>
    </svg>
    <span class="web">www.vantorelprestige.example</span>
  </section>

  <section class="sheet card card-front" aria-label="Business card front">
    <div class="gold-bar"></div>
    <div class="brand"><span class="brand-dot"></span><span class="brand-name">VantorelPrestige</span></div>
    <address class="contact">
      47219 Brookfern Hollow Lane<br>
      Larkmont, Ohio 30982<br>
      P: 555-201-0142<br>
      F: 555-201-0143<br>
      mlind@vantorelprestige.example
    </address>
    <svg class="swoosh" viewBox="0 0 278 58" preserveAspectRatio="none" aria-hidden="true">
      <defs>
        <linearGradient id="cf-band" x1="0" y1="0" x2="1" y2="0">
          <stop offset="0" stop-color="#3a56c9"/>
          <stop offset=".5" stop-color="#1f2a8a"/>
          <stop offset="1" stop-color="#10134a"/>
        </linearGradient>
      </defs>
      <path d="M0 40 C100 36 200 22 278 0 L278 58 L0 58 Z" fill="url(#cf-band)"/>
    </svg>
    <p class="holder">Marc Lindqvora <span class="title">– President</span></p>
  </section>

  <section class="sheet card card-back" aria-label="Business card back">
    <div class="gold-bar"></div>
    <svg class="swoosh" viewBox="0 0 278 58" preserveAspectRatio="none" aria-hidden="true">
      <defs>
        <linearGradient id="cb-band" x1="0" y1="0" x2="1" y2="0">
          <stop offset="0" stop-color="#3a56c9"/>
          <stop offset=".5" stop-color="#1f2a8a"/>
          <stop offset="1" stop-color="#10134a"/>
        </linearGradient>
      </defs>
      <path d="M0 40 C100 36 200 22 278 0 L278 58 L0 58 Z" fill="url(#cb-band)"/>
    </svg>
    <span class="web">www.vantorelprestige.example</span>
  </section>

</body>
</html>
```